Nine Lanterns Rollup Banner/Poster

I provide a Personalised Baby Planning and Maternity Concierge service and I will have a couple of Trade Fair events this year for which I'd like to have a roll-up banner/poster designed. In a nutshell, Nine Lanterns is a Baby Planning service that helps busy moms and dads by providing guidance, support and education to them in a tailored and unbiased manner. Think of us as a personal assistant in all things pregnancy-related. The company colour schemes can be found on our website at http://www.ninelanterns.com.sg - I also have business cards and brochures and can share these designs with you so you get the idea.
--------------------------------------------------------------
TEXT to be on the poster:

The arrival of a new baby can be both exciting and stressful. Let us guide you in making the decisions that are best for your family.

Nine Lanterns is a Baby Planning service that helps busy moms and dads by providing guidance, support and education to them in a tailored and unbiased manner. Think of us as your personal assistant in all things pregnancy-related. Enjoy your pregnancy journey and make well-informed decisions with confidence, but without the stress!

www.ninelanterns.com.sg

An idea would be to have a picture of a mom (of Asian origin) with some thought bubbles containing text like:
- Baby names?
- Birth planning?
- Childbirth classes?
- Baby products?
- Childcare options?
- Full month planning?

Hope it doesn't get too crowded - if it does, we can discuss some changes!

Regards,
Corinne
www.ninelanterns.com.sg
Updates

Hi all, Thanks for the first few designs. I think perhaps all that text might be too crowded. Perhaps better to propose design only with the following text: -------------------- The arrival of a new baby can be both exciting and stressful. Let us guide you in making the decisions that are best for your family. www.ninelanterns.com.sg -------------------- The thought bubbles can remain - I like them! :-)

Hi as another note - I noticed everyone submitted designs only using the TEAL colour. There's also a small touch of pink on my website.... could you incorporate that in the design in a subtle way somewhere please? That would be nice :-)

Target Market(s)

My target market are pregnant moms! Especially first-time moms.

Industry/Entity Type

Education

Requirements
Must have
• The poster size must be 200cm tall x 85cm wide. There needs to be some margin or bleed area of course. The resolution needs to be a minimum of 300 dpi at actual size.

Please keep to the Nine Lanterns colour scheme provided in the attached images (business card and brochures).

```html
<!DOCTYPE html>
<html lang="en">
<head>
<meta charset="utf-8">
<title>Nine Lanterns – Roll-up Banner</title>
<link rel="stylesheet" href="https://fonts.googleapis.com/css2?family=Jost:wght@500;600&family=Crimson+Text&family=Open+Sans:wght@600&display=swap">
<style>
  :root {
    --teal: #6acad1;
    --ink: #1f1f1f;
    --white: #ffffff;
    --body-grey: #8c8c8c;
    --label-grey: #5a5a5a;
    --frame: #b5b5b5;
    --photo-top: #ffffff;
    --photo-mid: #f0eeec;
    --photo-bottom: #dcdcdc;
  }
  * { margin: 0; padding: 0; box-sizing: border-box; }
  html, body {
    width: 1200px; height: 1000px; overflow: hidden;
    background: var(--white);
  }
  .banner {
    position: absolute;
    left: 411px; top: 57px;
    width: 378px; height: 887px;
    border: 1px solid var(--frame);
    background: var(--white);
    display: flex; flex-direction: column;
  }
  .banner__header {
    height: 100px;
    background: var(--teal);
    display: flex; align-items: center; justify-content: center;
  }
  .brand-name {
    font-family: "Jost", sans-serif;
    font-weight: 600;
    font-size: 40px;
    color: var(--ink);
  }
  .banner__visual {
    position: relative;
    height: 286px;
  }
  .photo-placeholder {
    position: absolute; inset: 0;
    background: linear-gradient(180deg, var(--photo-top) 0%, var(--photo-mid) 55%, var(--photo-bottom) 100%);
  }
  .thought {
    position: absolute;
    font-family: "Open Sans", sans-serif;
    font-weight: 600;
    font-size: 9.5px;
    line-height: 11px;
    color: var(--label-grey);
    text-align: center;
    white-space: nowrap;
    transform: translateX(-50%);
  }
  .banner__tagline {
    height: 162px;
    background: var(--teal);
    display: flex; align-items: center; justify-content: center;
  }
  .tagline {
    font-family: "Jost", sans-serif;
    font-weight: 500;
    font-size: 21px;
    line-height: 29px;
    color: var(--white);
    text-align: center;
    white-space: nowrap;
  }
  .banner__about {
    height: 243px;
    padding: 20px 10px 0 27px;
  }
  .about {
    font-family: "Crimson Text", serif;
    font-size: 17px;
    line-height: 26px;
    color: var(--body-grey);
    white-space: nowrap;
  }
  .banner__footer {
    flex: 1;
    background: var(--teal);
    display: flex; align-items: center; justify-content: center;
  }
  .web-address {
    font-family: "Crimson Text", serif;
    font-size: 30px;
    color: var(--ink);
    white-space: nowrap;
  }
</style>
</head>
<body>
  <main class="banner">
    <header class="banner__header">
      <span class="brand-name">Nine Lanterns</span>
    </header>

    <section class="banner__visual">
      <div class="photo-placeholder" role="img" aria-label="Photo of an expectant Asian mother in a white dress, looking down and holding her bump, with a dotted ring of questions circling above her head"></div>
      <span class="thought" style="left:148px; top:21px;">Birth<br>planning?</span>
      <span class="thought" style="left:190px; top:5px;">Childbirth<br>classes?</span>
      <span class="thought" style="left:247px; top:0px;">Baby<br>products?</span>
      <span class="thought" style="left:304px; top:14px;">Childcare<br>options?</span>
      <span class="thought" style="left:172px; top:43px;">Baby<br>names?</span>
      <span class="thought" style="left:320px; top:36px;">Full<br>month<br>planning?</span>
    </section>

    <section class="banner__tagline">
      <p class="tagline">The arrival of a new baby can be<br>both exciting and stressful.<br>Let us guide you in making the<br>decisions that are best for your<br>family.</p>
    </section>

    <section class="banner__about">
      <p class="about">Nine Lanterns is a Baby Planning service that<br>helps busy moms and dads by providing<br>guidance, support and education to them<br>in a tailored and unbiased manner. Think<br>of us as your personal assistant in all things<br>pregnancy-related. Enjoy your pregnancy<br>journey and make well-informed decisions<br>with confidence, but without the stress!</p>
    </section>

    <footer class="banner__footer">
      <span class="web-address">www.ninelanterns.com.sg</span>
    </footer>
  </main>
</body>
</html>
```